TECH PROJECT NEEDS NEW SKINS FOR RE-BRANDING

We are a technology project that has a product (crypto wallet) nearing release, have basic designs made so far however we need NEW SKINS/ branding/ design options for this wallet to change the look and feel -- it will be called and re-branded as "KESTRIL" a futuristic/ space/ edgy product so need it to look like so.

YOU ARE ALLOWED TO CHANGE + EXPERIMENT WITH THE LAYOUT/ schema and UI as you see fit -- (we are open to new and creative ideas)

(see WALLET.PNG and PROTFOLIO.PNG ATTACHED --- these are the pages we need new skins for )

(see KESTRIL logo attached --- PLEASE USE THIS LOGO/ VERSIONS OF THIS LOGO IN YOUR DESIGNS/SKIN SUBMISSIONS -- WE PROVIDED THE ai file so feel free to alter the logo a bit to experiment if you want -- we are open and flexible to new creative ideas)

(FOR A MOOD BOARD FOR GUIDANCE on feel/colors/mood-- SEE "SAMPLE INTERFACE 1 & 2" ATTACHED)

Target Market(s)

TECHNOLOGY/SPACE/ FUTURE

Number of Pages Required

2 page

Colors

Designer to choose colors to be used in the design.

Requirements
Must have
• MUST USE OUR KESTRIL LOGO OR A SIMILAR ALTERATION OF IT

```html
<!DOCTYPE html>
<html lang="en">
<head>
<meta charset="utf-8">
<title>KESTRIL Wallet Dashboard</title>
<link href="https://fonts.googleapis.com/css2?family=Roboto:wght@400;500;700;900&display=swap" rel="stylesheet">
<style>
  :root{
    --space:#060a14;
    --topbar:#000000;
    --nav:#101a30;
    --nav-edge:#1e3a5c;
    --card:#0d1526;
    --card-edge:#1d3354;
    --band-top:#1c3050;
    --text:#eef4ff;
    --muted:#7f8ea8;
    --accent:#27e1ff;
    --accent-2:#7a5cff;
    --line:#1f2c46;
    --green:#36f06a;
    --green-badge:#2fb860;
    --red:#ff3b4e;
    --avatar:#8fe98f;
    --faint:#34425e;
    --glow:0 0 0 1px var(--card-edge),0 0 14px rgba(39,225,255,.12);
  }
  *{box-sizing:border-box;margin:0;padding:0}
  html,body{width:1200px;height:960px;overflow:hidden;background:var(--space)}
  body{position:relative;font-family:"Roboto",Arial,sans-serif;color:var(--text);
    background:radial-gradient(ellipse at 70% 10%,#101c36 0%,var(--space) 60%)}

  .topbar{position:absolute;left:0;top:0;width:1200px;height:89px;background:var(--topbar);border-bottom:1px solid var(--nav-edge)}
  .brand{position:absolute;left:92px;top:28px;display:flex;align-items:center;gap:10px;color:var(--text);font-weight:500;font-size:24px;letter-spacing:3px}
  .brand-mark{width:20px;height:20px;border:3px solid var(--accent);border-radius:3px}
  .bell{position:absolute;left:874px;top:28px}
  .avatar{position:absolute;left:921px;top:13px;width:62px;height:62px;border-radius:50%;background:var(--avatar);box-shadow:0 0 0 2px var(--accent)}
  .user{position:absolute;left:992px;top:34px;color:var(--text);font-weight:500;font-size:16px;display:flex;align-items:center;gap:10px}

  .navbar{position:absolute;left:0;top:89px;width:1200px;height:44px;background:var(--nav);border-bottom:1px solid var(--nav-edge)}
  .nav-item{position:absolute;top:10px;color:var(--text);font-weight:500;font-size:21px;display:flex;align-items:center;gap:7px}
  .nav-item.active{color:var(--accent)}
  .nav-settings{position:absolute;left:1095px;top:10px}

  .card{position:absolute;background:var(--card);box-shadow:var(--glow);border-radius:4px}

  .balance-card{left:86px;top:177px;width:347px;height:711px;overflow:hidden}
  .balance-bg{position:absolute;left:0;top:0}
  .balance-label{position:absolute;top:42px;width:100%;text-align:center;font-size:15px;font-weight:500;letter-spacing:.3px;color:var(--muted)}
  .balance-value{position:absolute;top:64px;width:100%;text-align:center;font-size:31px;font-weight:700}
  .balance-value small{font-size:20px}
  .badge{position:absolute;left:138px;top:112px;width:71px;height:18px;background:var(--green-badge);color:#fff;font-size:15px;font-weight:500;text-align:center;line-height:18px;border-radius:2px}
  .pill{position:absolute;height:26px;border-radius:13px;background:linear-gradient(90deg,var(--accent-2),var(--accent));color:#fff;font-weight:700;font-size:15px;text-align:center;line-height:26px;box-shadow:0 0 10px rgba(39,225,255,.35)}
  .search{position:absolute;left:41px;top:257px;width:266px;height:26px;border:2px solid var(--accent);border-radius:6px;background:var(--space);font-size:16px;padding-left:13px;line-height:22px;color:var(--text)}
  .search svg{position:absolute;right:11px;top:3px}
  .section-title{position:absolute;left:20px;top:304px;font-size:26px;font-weight:700}
  .asset{position:absolute;left:28px;width:264px;height:60px}
  .asset-icon{position:absolute;left:0;top:17px;width:26px;height:26px;border-radius:50%}
  .asset-name{position:absolute;left:40px;top:20px;font-size:17px;font-weight:700}
  .asset-qty{position:absolute;right:0;top:10px;font-size:16px;font-weight:700;text-align:right;white-space:nowrap}
  .asset-fiat{display:block;font-size:10px;font-weight:400;color:var(--muted)}
  .divider{position:absolute;left:28px;width:268px;height:2px;background:var(--line)}
  .scrollbar{position:absolute;left:323px;top:431px;width:3px;height:88px;background:var(--accent);border-radius:2px}

  .tx-card{left:442px;top:177px;width:666px;height:444px;overflow:hidden}
  .tx-title{position:absolute;top:30px;width:100%;text-align:center;font-size:21px;font-weight:900;letter-spacing:.5px}
  .tx-head,.tx-row{position:absolute;left:0;width:100%;font-size:14px}
  .tx-head{top:106px;color:var(--muted)}
  .tx-head span,.tx-row span{position:absolute;white-space:nowrap}
  .tx-row{font-weight:700}
  .tx-row .addr{font-weight:400;color:#c9d4e8}
  .amt{right:34px;text-align:right}
  .amt .fiat{display:block;font-size:7px;color:var(--faint);font-weight:400}
  .plus{color:var(--green)}
  .minus{color:var(--red)}

  .address-card{left:442px;top:631px;width:400px;height:257px}
  .address-title{position:absolute;left:23px;top:63px;font-size:27px;font-weight:700}
  .address-value{position:absolute;left:23px;top:110px;font-size:16px;letter-spacing:.3px;color:#c9d4e8}
  .copy-icon{position:absolute;left:360px;top:109px}

  .help-card{left:853px;top:631px;width:257px;height:257px;overflow:hidden}
  .help-art{position:absolute;left:0;top:0}
  .help-title{position:absolute;left:0;width:100%;top:70px;font-size:32px;font-weight:900;line-height:38px;text-align:center}
</style>
</head>
<body>

<header class="topbar">
  <div class="brand"><span class="brand-mark"></span>KESTRIL</div>
  <svg class="bell" width="28" height="30" viewBox="0 0 28 30" aria-hidden="true">
    <path d="M4 22 Q7 19 7 13 Q7 5 14 5 Q21 5 21 13 Q21 19 24 22 Z" fill="#eef4ff"/>
    <circle cx="14" cy="25.5" r="3" fill="#eef4ff"/>
    <circle cx="21" cy="6" r="4" fill="#27e1ff"/>
  </svg>
  <div class="avatar"></div>
  <div class="user">Rowan Vale
    <svg width="14" height="10" viewBox="0 0 14 10" aria-hidden="true"><path d="M2 2 L7 7 L12 2" fill="none" stroke="#eef4ff" stroke-width="2.6"/></svg>
  </div>
</header>

<nav class="navbar">
  <div class="nav-item active" style="left:76px">
    <svg width="20" height="12" viewBox="0 0 20 12" aria-hidden="true"><path d="M2 11 A8 8 0 0 1 18 11" fill="none" stroke="#27e1ff" stroke-width="2"/><path d="M10 11 L14 5" stroke="#27e1ff" stroke-width="2"/></svg>Dashboard</div>
  <div class="nav-item" style="left:288px">
    <svg width="20" height="20" viewBox="0 0 20 20" aria-hidden="true"><rect x="1" y="12" width="4" height="8" fill="#eef4ff"/><rect x="7" y="8" width="4" height="12" fill="#eef4ff"/><rect x="13" y="5" width="4" height="15" fill="#eef4ff"/><path d="M1 9 L8 3 L12 6 L19 0" stroke="#eef4ff" stroke-width="2" fill="none"/></svg>Portfolio</div>
  <div class="nav-item" style="left:478px">
    <svg width="20" height="16" viewBox="0 0 20 16" aria-hidden="true"><rect x="0" y="2" width="19" height="13" rx="2" fill="#eef4ff"/><rect x="12" y="6" width="7" height="5" fill="#101a30"/></svg>Wallet</div>
  <div class="nav-item" style="left:647px">
    <svg width="18" height="20" viewBox="0 0 18 20" aria-hidden="true"><path d="M9 0 L3 11 L8 11 L5 20 L15 7 L10 7 L13 0 Z" fill="#eef4ff"/></svg>Lighting</div>
  <div class="nav-item" style="left:832px">
    <svg width="22" height="14" viewBox="0 0 22 14" aria-hidden="true"><path d="M5 14 Q0 14 0 10 Q0 6 5 6 Q6 0 12 1 Q17 2 17 7 Q22 7 22 11 Q22 14 18 14 Z" fill="#eef4ff"/></svg>ORB Cloud</div>
  <svg class="nav-settings" width="24" height="24" viewBox="0 0 24 24" aria-hidden="true">
    <g fill="#eef4ff"><circle cx="12" cy="12" r="8"/>
      <rect x="10" y="0" width="4" height="24"/><rect x="0" y="10" width="24" height="4"/>
      <rect x="10" y="0" width="4" height="24" transform="rotate(45 12 12)"/><rect x="10" y="0" width="4" height="24" transform="rotate(-45 12 12)"/></g>
    <circle cx="12" cy="12" r="4" fill="#101a30"/>
  </svg>
</nav>

<section class="card balance-card">
  <svg class="balance-bg" width="347" height="300" viewBox="0 0 347 300" aria-hidden="true">
    <defs>
      <linearGradient id="bandFade" x1="0" y1="0" x2="0" y2="1">
        <stop offset="0" stop-color="#1c3050"/>
        <stop offset="1" stop-color="#0d1526"/>
      </linearGradient>
    </defs>
    <path d="M0 150 Q173 290 347 150 L347 300 L0 300 Z" fill="url(#bandFade)"/>
    <path d="M0 158 Q173 298 347 158" fill="none" stroke="#27e1ff" stroke-opacity=".55" stroke-width="3"/>
  </svg>
  <div class="balance-label">TOTAL BALANCE</div>
  <div class="balance-value"><small>R</small>$7.000,00</div>
  <div class="badge">+5.00%</div>
  <div class="pill" style="left:58px;top:146px;width:110px">Deposit</div>
  <div class="pill" style="left:178px;top:146px;width:110px">Withdrawal</div>
  <div class="search">Search
    <svg width="18" height="18" viewBox="0 0 18 18" aria-hidden="true"><circle cx="7.5" cy="7.5" r="6" fill="none" stroke="#27e1ff" stroke-width="2"/><path d="M12 12 L17 17" stroke="#27e1ff" stroke-width="2"/></svg>
  </div>
  <h2 class="section-title">Portfolio</h2>

  <div class="asset" style="top:360px"><span class="asset-icon" style="background:#f7931a"></span><span class="asset-name">Quasar</span><span class="asset-qty">0,1827&nbsp; QSR<span class="asset-fiat">(R$ 6.000,00)</span></span></div>
  <div class="divider" style="top:423px"></div>
  <div class="asset" style="top:430px"><span class="asset-icon" style="background:#8c8c8c"></span><span class="asset-name">Photon</span><span class="asset-qty">1,3790&nbsp; PHT<span class="asset-fiat">(R$ 1.000,00)</span></span></div>
  <div class="divider" style="top:493px"></div>
  <div class="asset" style="top:498px"><span class="asset-icon" style="background:#8dc351"></span><span class="asset-name">Quasar Cash</span><span class="asset-qty">0,0000&nbsp; QSC<span class="asset-fiat">(R$ 0,00)</span></span></div>
  <div class="divider" style="top:563px"></div>
  <div class="asset" style="top:568px"><span class="asset-icon" style="background:#7b86ee"></span><span class="asset-name">Nebula</span><span class="asset-qty">3,2570&nbsp; NBL<span class="asset-fiat">(R$ 3.000,00)</span></span></div>
  <div class="divider" style="top:631px"></div>
  <div class="asset" style="top:638px"><span class="asset-icon" style="background:#1b8ed3"></span><span class="asset-name">Pulsar</span><span class="asset-qty">0,0000&nbsp; PLS<span class="asset-fiat">(R$ 0,00)</span></span></div>
  <div class="scrollbar"></div>
</section>

<section class="card tx-card">
  <svg style="position:absolute;left:0;top:0" width="666" height="90" viewBox="0 0 666 90" aria-hidden="true">
    <defs>
      <linearGradient id="txFade" x1="0" y1="0" x2="0" y2="1">
        <stop offset="0" stop-color="#1c3050"/>
        <stop offset="1" stop-color="#0d1526"/>
      </linearGradient>
    </defs>
    <path d="M0 0 H666 V75 Q333 -10 0 75 Z" fill="url(#txFade)"/>
    <path d="M0 78 Q333 -4 666 78" fill="none" stroke="#27e1ff" stroke-opacity=".55" stroke-width="2"/>
  </svg>
  <h2 class="tx-title">LAST TRANSICTIONS</h2>
  <div class="tx-head"><span style="left:40px">Name :</span><span style="left:190px">Date :</span><span style="left:311px">Address :</span><span style="right:39px">Amount :</span></div>
  <div class="tx-row" style="top:150px"><span style="left:34px">Corvex</span><span style="left:181px">30/03/2019</span><span class="addr" style="left:304px">From :&nbsp; 1h78jkdfUYTtvhjgjfw375utyiit...</span><span class="amt plus">+0,01 QSR<span class="fiat">(R$ 5000,0)</span></span></div>
  <div class="tx-row" style="top:197px"><span style="left:34px">aaa@mailnest.io</span><span style="left:182px">26/03/2019</span><span class="addr" style="left:302px">To :&nbsp; 1h78jkdfUYTtvhjgjfw375utyiit...</span><span class="amt minus">-0,003 QSR<span class="fiat">(R$ 50,0)</span></span></div>
  <div class="tx-row" style="top:247px"><span style="left:36px">Rowan@mailnest.io</span><span style="left:182px">26/03/2019</span><span class="addr" style="left:305px">To :&nbsp; 1h78jkdfUYTtvhjgjfw375utyiit...</span><span class="amt minus">-1,00 NBL<span class="fiat">(R$ 900,0)</span></span></div>
  <div class="tx-row" style="top:297px"><span style="left:34px">rowanvcdccv@...</span><span style="left:181px">20/03/2019</span><span class="addr" style="left:304px">From :&nbsp; 1h78jkdfUYTtvhjgjfw375utyiit...</span><span class="amt plus">+1,00 PHT<span class="fiat">(R$ 3000,0)</span></span></div>
  <div class="tx-row" style="top:346px"><span style="left:34px">yourname@inf....</span><span style="left:182px">20/03/2019</span><span class="addr" style="left:304px">From :&nbsp; 1h78jkdfUYTtvhjgjfw375utyiit...</span><span class="amt plus">+0,17 PHT<span class="fiat">(R$ 100,0)</span></span></div>
  <div class="pill" style="left:278px;top:385px;width:111px">SEE ALL</div>
</section>

<section class="card address-card">
  <h2 class="address-title">My Address :</h2>
  <div class="address-value">17VhtrfIgfdc1uhjh9qtobs7eTjklglzxGJklOas</div>
  <svg class="copy-icon" width="16" height="18" viewBox="0 0 16 18" aria-hidden="true">
    <rect x="4" y="1" width="11" height="13" rx="1" fill="#0d1526" stroke="#27e1ff" stroke-width="1.4"/>
    <rect x="1" y="4" width="11" height="13" rx="1" fill="#0d1526" stroke="#27e1ff" stroke-width="1.4"/>
    <path d="M3.5 8 H9.5 M3.5 11 H9.5 M3.5 14 H9.5" stroke="#27e1ff" stroke-width="1.2"/>
  </svg>
  <div class="pill" style="left:101px;top:163px;width:199px">Manage your address</div>
</section>

<section class="card help-card">
  <svg class="help-art" width="257" height="257" viewBox="0 0 257 257" role="img" aria-label="Soft chat bubble backdrop">
    <defs>
      <linearGradient id="helpFade" x1="0" y1="0" x2="0" y2="1">
        <stop offset="0" stop-color="#22385c"/>
        <stop offset="1" stop-color="#0f1a2e"/>
      </linearGradient>
    </defs>
    <path d="M100 0 H257 V200 L230 190 Q175 180 130 140 Q95 100 100 0 Z" fill="url(#helpFade)"/>
  </svg>
  <h2 class="help-title">Need<br>Help ?</h2>
  <div class="pill" style="left:38px;top:173px;width:178px">Get in touch</div>
</section>

</body>
</html>
```